We need your help in designing the graphical look of the home page of our web site: Quellnest.com.

Quellnest is an FREE online service that brings consumers and service providers together through online reservations.

Our service is in fact a web application (similar to brindlo calendar), so we will be using forms, widgets, menus and standard web controls (buttons, fields, links, etc). We need a design that will be easy to integrate with our programming.

This design project is for the HOME page, but we will choose the designer that will design the web page in photoshop in layers, so we can easily derive our other secondary pages ourselves.

If you have any questions please send us a message and we will gladly update the brief with a response.

Happy Designing!
Updates

Hi all, the menu on the home page should be something standard, like: Pricing, features, how it works.

once a user is logged in, they will see their toolbox at all times:
- My Nest (links to their main page of bookings)
- My Faborites (view favorite businesses and book quickly with them)
- Settings (set parameters of their account)

There should be a My Profile page as well. 

Thanks!

Reason: I have extended the deadline to receive more designs.

Hi All,

UPDATE: we changed our vision of the home page to have a much simpler design.  something along the lines of tumbrella vexnor and mor tan.

HOME PAGE:
light colors with white background.  simple, simple, simple!

header should not be big, logo, change language link. try with search bar (what and where).

body should be simple, with an image + register form only.

footer with links to pages for more info:
- Privacy,
- Getting started
- How it works
- Contact us
- FAQ
- Pricing

LOGGED IN PAGE:
when logged in, the header can be the same or reduced to maximize the "working area" (body).
body can be a 2 or 3 column design, as we have a main working area.  in your design, show a calendar.  we need a toolbar (side or top) that will have these buttons, links: MyNest, My Favorites, Settings, My Profile.
We need a section that will display latest messages or notifications.
keep the footer with the links.

Thank you all.

Reason: Holidays

Reason: holidays... lets spend time with our families!

Target Market(s)

Young and mobile consumers + professionals, businesses, restaurants and commerces wishing to offer online reservations (appointments and reservations)

Industry/Entity Type

Brindlo

Requirements
Must have
• - Easy to integrate with web programming
- light weight visual design. We want something with light tone colors as background
- home page will have a content slider that will show some catch phrases.
- Overall design should be more on the "cartoony" side. Should give a casual, humour and friendly ambiance.

The home page should have these sections:
- a search section for consumers to find local businesses. They will search by specifying "What?" & "Where?"
- a content slider that will cycle through catch phrases and features. Each pane should have an image representative of the text.
- have 4 highlighted sections
- QuellNest is great for (list of different businesses types that use quelnest)
- QuellNest is available for FREE to everyone
- Main features list (accept 24/7 reservations, never reveal your schedule, automatic reminders, marketing campaigns)
- The more you quell, the more you save! (info on our loyalty program that entitles consumers to greater savings and benefits).

One a user logs in, all the certer page info will be replaced by a content div that will allow content to display based on selected menu item
- My Nest (opens the main section where all happens. This section should have a design that gives the impression that we're looking in a box)
- My Profile
- My Favorites
Should not have
• - Don't use actual photos of real people, rather opt for sketches and cartoony characters.

```html
<!DOCTYPE html>
<html lang="en">
<head>
<meta charset="utf-8">
<title>QuellNest – Home</title>
<link rel="stylesheet" href="https://fonts.googleapis.com/css2?family=Open+Sans:ital,wght@0,400;0,600;0,700;1,400&display=swap">
<style>
:root{
  --orange:#f39200;
  --orange-dark:#ec8400;
  --amber:#f7b500;
  --yellow:#fdd63a;
  --sky-top:#2fa4ea;
  --sky-bottom:#d6f0fc;
  --ink:#4a4a4a;
  --teal-ink:#1d5a78;
  --white:#ffffff;
  --panel:#f5f5f5;
  --green:#8fd63a;
  --blue:#39ace0;
  --tangerine:#f7911e;
  --footer:#2c2c2c;
  --footer-bar:#3a3a3a;
  --footer-head:#444444;
  --footer-text:#c9c9c9;
}
*{box-sizing:border-box;margin:0;padding:0}
html,body{width:931px;height:1200px;overflow:hidden;background:var(--white)}
body{font-family:"Open Sans",Verdana,sans-serif;color:var(--ink);position:relative}
.abs{position:absolute}

/* header */
.topbar{left:0;top:0;width:931px;height:44px;background:linear-gradient(#ffc64a,#f7a21a)}
.logo{left:46px;top:0;width:126px;height:130px;background:var(--white);box-shadow:0 2px 6px rgba(0,0,0,.3);display:flex;flex-direction:column;align-items:center;justify-content:center;gap:10px;z-index:3}
.logo-mark{width:52px;height:52px;background:var(--amber)}
.logo-name{font-size:15px;font-weight:700;color:var(--orange);letter-spacing:.5px}
.welcome{left:179px;top:13px;width:133px;height:20px;background:var(--yellow);font-size:13px;line-height:20px;text-align:center;color:#5a3a00}
.nav{left:340px;top:11px;display:flex;align-items:center;font-size:13px;color:#4b3200}
.nav a{color:inherit;text-decoration:none;padding:4px 7px;border-radius:3px}
.nav .sep{margin:0 6px;color:#7a5a10}
.nav .active{background:var(--orange);color:var(--white)}
.lang{left:793px;top:13px;width:99px;height:20px;border-radius:4px;background:linear-gradient(#fff,#e6e6e6);border:1px solid #b9b9b9;font-size:12px;line-height:18px;padding-left:6px;color:#555}
.lang::after{content:"";position:absolute;right:0;top:0;width:18px;height:18px;background:#888;border-radius:0 3px 3px 0}

/* hero */
.hero{left:0;top:44px;width:931px;height:336px;background:linear-gradient(var(--sky-top),#7cc9f2 60%,var(--sky-bottom));overflow:hidden}
.clouds{left:0;top:250px;width:931px;height:90px;background:linear-gradient(rgba(255,255,255,0),#fff 70%)}
.search{left:303px;top:25px;display:flex}
.search-field{width:272px;height:22px;background:#fff;border:1px solid #bbb;border-radius:3px 0 0 3px;font-size:12px;line-height:20px;padding-left:8px;color:#777}
.search-btn{width:76px;height:22px;background:linear-gradient(#fff,#e3e3e3);border:1px solid #aaa;border-radius:0 3px 3px 0;font-size:12px;line-height:20px;text-align:center;color:#555}
.punch{left:108px;top:134px;font-size:24px;line-height:28px;color:var(--teal-ink)}
.punch strong{font-weight:700}
.hero-art{left:370px;top:76px;width:295px;height:250px;border-radius:40px;background:radial-gradient(circle at 50% 45%,#f6d64a,#8a7ae0 55%,rgba(120,190,240,0) 72%)}
.slide-arrow{top:138px}

/* highlight box */
.highlights{left:35px;top:409px;width:545px;height:263px;border-radius:4px;overflow:hidden;display:flex}
.hl{position:relative;color:var(--white);font-size:11px;line-height:13px}
.hl-great{width:244px;background:var(--orange);padding:52px 16px 0 21px}
.hl-fee{flex:1;background:var(--amber);padding:52px 10px 0 12px}
.hl-title{position:absolute;top:0;font-size:15px;line-height:20px}
.hl-title .tab{display:inline-block;background:var(--white);color:var(--orange);padding:18px 4px 6px 3px;border-radius:0 0 3px 3px}
.hl-great .hl-title{left:21px}
.hl-fee .hl-title{left:13px}
.hl-title .rest{color:var(--white)}
.read-btn{display:inline-block;margin-top:12px;background:var(--yellow);color:#7a4a00;font-size:11px;padding:2px 6px;border-radius:3px}
.fee-item{display:flex;gap:12px;align-items:flex-start;margin-bottom:15px}
.fee-item:first-of-type{margin-top:-6px}
.fee-icon{flex:none;width:50px;height:50px;border-radius:50%;background:radial-gradient(#fff 45%,#f7d9b0 46%,#e96c2a);box-shadow:0 1px 3px rgba(0,0,0,.3)}

/* video */
.video{left:600px;top:409px;width:277px;height:188px;background:var(--panel);border:3px solid #e6e6e6}
.video-label{left:0;top:72px;width:277px;text-align:center;font-size:11px;color:#444}
.video-stand{left:598px;top:590px}

/* features */
.features-title{left:603px;top:686px;display:flex;align-items:center;font-size:16px;color:var(--orange)}
.bubble{width:46px;height:30px;background:var(--orange);border-radius:50%;color:#fff;text-align:center;line-height:30px;margin-right:4px}
.feature{left:608px;width:265px;height:75px;display:flex}
.feature-icon{width:76px;display:flex;align-items:center;justify-content:center}
.feature-text{flex:1;padding:6px 8px;font-size:10.5px;line-height:12px;color:#fff}
.feature-text b{display:block;font-weight:400;color:#111;font-size:10.5px}

/* loyalty */
.loyalty{left:36px;top:706px;width:545px}
.loyalty h2{font-size:16px;font-weight:400;color:var(--orange);line-height:20px}
.loyalty .lead{font-size:11.5px;font-style:italic;color:var(--orange);line-height:14px;margin-bottom:7px}
.loyalty p{font-size:11.5px;line-height:13px;color:#555;padding-left:1px}
.loyalty p+p{margin-top:13px}
.read-more{margin-top:14px;display:flex;align-items:center;font-size:11px;color:#666}
.read-more .bubble{width:40px;height:26px;line-height:26px;font-size:11px;background:var(--amber);margin-right:2px}

/* footer */
.footer{left:0;top:998px;width:931px;height:164px;background:var(--footer)}
.footer-bar{left:0;top:1162px;width:931px;height:38px;background:var(--footer-bar);color:var(--footer-text);font-size:11px;line-height:38px;padding-left:643px}
.fcol{top:14px;width:156px}
.fcol h3{height:22px;background:var(--footer-head);font-size:12.5px;font-weight:400;color:#eee;line-height:22px;padding-left:12px}
.fcol ul{list-style:none;margin-top:9px;padding-left:4px}
.fcol li{font-size:12.5px;color:var(--footer-text);line-height:19px;display:flex;align-items:center;gap:4px}
.social{display:flex;gap:5px;margin:12px 0 0 55px;flex-wrap:wrap;width:100px}
.social span{font-size:8px;color:#ddd;line-height:10px}
</style>
</head>
<body>

<header>
  <div class="abs topbar"></div>
  <div class="abs logo"><div class="logo-mark"></div><div class="logo-name">QuellNest</div></div>
  <div class="abs welcome">welcome user, name</div>
  <nav class="abs nav">
    <a>Main page</a><span class="sep">|</span>
    <a class="active">My Nest</a><span class="sep">|</span>
    <a>My Profile</a><span class="sep">|</span>
    <a>My Favorite</a><span class="sep">|</span>
    <a>Settings</a>
  </nav>
  <div class="abs lang">English</div>
</header>

<section class="abs hero">
  <div class="abs clouds"></div>
  <div class="abs search"><div class="search-field">search business...</div><div class="search-btn">SEARCH</div></div>
  <div class="abs punch">Your Company Punch<br>line <strong>goes here...</strong></div>
  <div class="abs hero-art" role="img" aria-label="Cartoon businessman with briefcase riding a giant yellow and purple mobile phone on a leafy vine"></div>
  <svg class="abs slide-arrow" style="left:32px" width="28" height="50" viewBox="0 0 28 50"><path d="M14 2 2 25l12 23M26 2 14 25l12 23" fill="none" stroke="#fff" stroke-width="4"/></svg>
  <svg class="abs slide-arrow" style="left:862px" width="28" height="50" viewBox="0 0 28 50"><path d="M2 2l12 23L2 48M14 2l12 23-12 23" fill="none" stroke="#fff" stroke-width="4"/></svg>
</section>

<section class="abs highlights">
  <div class="hl hl-great">
    <div class="hl-title"><span class="tab">Why</span> <span class="rest">Great ?</span></div>
    <p>Brightwave eSolutions provides you the Search Engine Optimization making your website search engine friendly.<br>So that the website can achieve top position and ranking in the Internet searches and thereby increasing the scope for the website to be found by customers. We here modify the site to improve the ranking by using the keywords and contents.</p>
    <span class="read-btn">read more</span>
  </div>
  <div class="hl hl-fee">
    <div class="hl-title"><span class="tab">Why</span> <span class="rest">Fee</span></div>
    <div class="fee-item"><div class="fee-icon" role="img" aria-label="Calculator icon"></div><p>Brightwave eSolutions provides you the Search Engine Optimization making your website search engine friendly.</p></div>
    <div class="fee-item"><div class="fee-icon" role="img" aria-label="Calendar page icon"></div><p>E-Commerce is a major progress in technology that has changed the way in which the customers now purchase information.</p></div>
    <div class="fee-item"><div class="fee-icon" role="img" aria-label="Presentation board icon"></div><p>E-Commerce is a major progress in technology that has changed the way in which the customers now purchase information.</p></div>
  </div>
</section>

<div class="abs video">
  <div class="abs video-label">How it works ?</div>
  <svg class="abs" style="left:126px;top:88px" width="26" height="30" viewBox="0 0 26 30"><path d="M0 0 26 15 0 30z" fill="#777"/></svg>
</div>
<svg class="abs video-stand" width="282" height="70" viewBox="0 0 282 70">
  <ellipse cx="141" cy="60" rx="90" ry="6" fill="#eee"/>
  <rect x="0" y="3" width="281" height="7" rx="2" fill="#2a2a2a"/>
  <path d="M141 10v38M141 26 88 52M141 26l54 24M141 48v10" stroke="#333" stroke-width="2" fill="none"/>
</svg>

<div class="abs features-title"><span class="bubble">Our</span>Features</div>
<div class="abs feature" style="top:730px">
  <div class="feature-icon" style="background:#eef8e2"><svg width="42" height="42" viewBox="0 0 42 42"><g fill="#1d8fd0"><circle cx="21" cy="21" r="13"/><g stroke="#1d8fd0" stroke-width="7"><path d="M21 2v38M2 21h38M7.5 7.5l27 27M34.5 7.5l-27 27"/></g></g><circle cx="21" cy="21" r="5" fill="#eef8e2"/></svg></div>
  <div class="feature-text" style="background:var(--green)"><b>HEADING HERE</b>E-Commerce is a major progress in technology that has changed the way in which the customers now purchase information</div>
</div>
<div class="abs feature" style="top:808px">
  <div class="feature-icon" style="background:#e3f2fa"><svg width="42" height="50" viewBox="0 0 42 50"><circle cx="14" cy="12" r="10" fill="#8a8f96"/><circle cx="14" cy="12" r="4" fill="#e3f2fa"/><path d="M19 19l18 26-5 3-3-5-3 2-2-4 3-2-12-16z" fill="#8a8f96"/></svg></div>
  <div class="feature-text" style="background:var(--blue)"><b>HEADING HERE</b>E-Commerce is a major progress in technology that has changed the way in which the customers now purchase information</div>
</div>
<div class="abs feature" style="top:887px">
  <div class="feature-icon" style="background:#fdf0e0"><svg width="42" height="42" viewBox="0 0 42 42"><path d="M36 4 40 8 14 34 8 36 10 30z" fill="#3f8f3a"/><path d="M10 30l4 4-8 4z" fill="#c9a24a"/></svg></div>
  <div class="feature-text" style="background:var(--tangerine)"><b>HEADING HERE</b>E-Commerce is a major progress in technology that has changed the way in which the customers now purchase information</div>
</div>

<section class="abs loyalty">
  <h2>Loyalty Program</h2>
  <div class="lead">Brightwave eSolutions is specialized in handling advanced web projects</div>
  <p>Static website are the which are usually been used and are benefited through the Professionals and Small Companies. The companies with fewer budgets can promote their products and services through the static website and gain a lot.</p>
  <p>To manage the static website HTML knowledge is the required. The simple website are also said as the static web as its embedded on a page.<br>Static website is a simple way to get your message out to the public. Static website are cheaper and also it needs less maintenance too. It’s the<br>simplest, cheapest and also the basic thing the search engine picks it up very easily. We at Bright wave provide you the best simple websites too<br>with total work done as using all the best designing and all done so that you can achieve the goal of yours through our work done on your website.</p>
  <div class="read-more"><span class="bubble">READ</span>MORE</div>
</section>

<footer>
  <div class="abs footer">
    <div class="abs fcol" style="left:50px">
      <h3>Our Links</h3>
      <ul><li>→ About Us</li><li>→ Our Company</li><li>→ Our Management</li><li>→ Contact info</li></ul>
    </div>
    <div class="abs fcol" style="left:222px">
      <h3>Feautred Services</h3>
      <ul><li>→ Basic Plan</li><li>→ Intermediate Plan</li><li>→ Advanced Plan</li></ul>
    </div>
    <div class="abs fcol" style="left:401px">
      <h3>Update with Us</h3>
      <div class="social"><span>mor tan</span><span>tumbrella</span><span>vexnor</span><span>vidlark</span></div>
    </div>
  </div>
  <div class="abs footer-bar">Copy right © 2011 Quellnest All right reserved</div>
</footer>

</body>
</html>
```